Banner Ad Design Project

We need banner ads for a website size:
728 x 90
160 x 90

Look at our website and you can see the color green we use throughout our advertising.

We have copy for 4 ads that should be interchangable

1. EHR me ASAP. Sign up in minutes.
2. Connect. Collaborate. Immediate. Sign up in minutes.
3. No software. No downloads. No charge.
4. EMR + HIE + PMR = FREE

Target Market(s)

Physicians

Industry/Entity Type

Software

```html
<!DOCTYPE html>
<html lang="en">
<head>
<meta charset="utf-8">
<title>Veradine Systems – Web Based EMR Banner</title>
<link href="https://fonts.googleapis.com/css2?family=Arimo:ital,wght@0,400;0,700;1,700&display=swap" rel="stylesheet">
<style>
  :root {
    --brand-green: #5aa21d;
    --brand-green-dark: #3f8412;
    --brand-green-light: #8cc63f;
    --alert-red: #d9231c;
    --alert-red-dark: #b3120e;
    --cta-yellow: #f8d21a;
    --cta-yellow-light: #fff27a;
    --cta-text: #8a1c10;
    --frame-grey: #b9b9b9;
    --white: #ffffff;
    --photo-light: #dfe6ea;
    --photo-mid: #a9c3d3;
  }
  * { box-sizing: border-box; margin: 0; padding: 0; }
  html, body { width: 1200px; height: 148px; overflow: hidden; background: var(--white); }
  .banner {
    position: relative; width: 1200px; height: 148px;
    border: 2px solid var(--frame-grey); background: var(--white);
    font-family: "Arimo", Arial, sans-serif; overflow: hidden;
  }
  .brand {
    position: absolute; left: 22px; top: 36px;
    display: flex; align-items: center; gap: 14px;
  }
  .brand-dot { width: 34px; height: 34px; border-radius: 50%; background: var(--brand-green); }
  .brand-name {
    color: var(--brand-green-dark); font-size: 30px; font-weight: 400; line-height: 1.05;
  }
  .team-photo {
    position: absolute; left: 338px; top: 0; width: 290px; height: 144px;
    background: linear-gradient(90deg, var(--photo-light), var(--photo-mid) 50%, var(--photo-light));
  }
  .offer {
    position: absolute; left: 610px; top: 0; width: 461px; height: 116px;
    background: linear-gradient(90deg, rgba(90,162,29,0) 0%, var(--brand-green) 14%, var(--brand-green-light) 60%, var(--brand-green) 100%);
    color: var(--white);
  }
  .offer-title {
    position: absolute; left: 64px; top: 12px;
    font-size: 28px; font-weight: 700; white-space: nowrap;
  }
  .benefits {
    position: absolute; left: 40px; top: 52px;
    display: grid; grid-template-columns: 150px 250px; row-gap: 6px;
    list-style: none;
  }
  .benefit {
    display: flex; align-items: center; gap: 8px;
    font-size: 23px; font-weight: 400; white-space: nowrap;
  }
  .benefit svg { width: 24px; height: 24px; flex: none; }
  .tagline {
    position: absolute; left: 610px; top: 116px; width: 461px; height: 28px;
    background: linear-gradient(180deg, var(--alert-red), var(--alert-red-dark));
    color: var(--white); font-size: 17px; font-weight: 700; font-style: italic;
    display: flex; align-items: center; justify-content: flex-end; padding-right: 10px;
    white-space: nowrap;
  }
  .cta {
    position: absolute; left: 1082px; top: 8px; width: 100px; height: 128px;
    border: 5px solid #9a9a9a; border-radius: 8px;
    background: linear-gradient(180deg, var(--cta-yellow-light), var(--cta-yellow) 55%, #e8b700);
    color: var(--cta-text); font-size: 27px; font-weight: 700; line-height: 1.2;
    display: flex; flex-direction: column; align-items: center; justify-content: center;
    text-align: center; text-decoration: none;
  }
</style>
</head>
<body>
  <div class="banner">
    <div class="brand">
      <span class="brand-dot"></span>
      <span class="brand-name">Veradine<br>Systems</span>
    </div>

    <div class="team-photo" role="img" aria-label="Photo of a team of smiling doctors in white coats with stethoscopes"></div>

    <div class="offer">
      <h1 class="offer-title">Best in class web based EMR</h1>
      <ul class="benefits">
        <li class="benefit"><svg viewBox="0 0 24 24"><path d="M3 13l6 6L21 5" fill="none" stroke="#fff" stroke-width="4" stroke-linecap="round" stroke-linejoin="round"/></svg>Free EMR</li>
        <li class="benefit"><svg viewBox="0 0 24 24"><path d="M3 13l6 6L21 5" fill="none" stroke="#fff" stroke-width="4" stroke-linecap="round" stroke-linejoin="round"/></svg>No software to install</li>
        <li class="benefit"><svg viewBox="0 0 24 24"><path d="M3 13l6 6L21 5" fill="none" stroke="#fff" stroke-width="4" stroke-linecap="round" stroke-linejoin="round"/></svg>No risks</li>
        <li class="benefit"><svg viewBox="0 0 24 24"><path d="M3 13l6 6L21 5" fill="none" stroke="#fff" stroke-width="4" stroke-linecap="round" stroke-linejoin="round"/></svg>fast to use</li>
      </ul>
    </div>

    <p class="tagline">Connect, Collaborate, Immediate. Sign Up in minutes.</p>

    <a class="cta" href="#"><span>FREE</span><span>Sign</span><span>Up</span></a>
  </div>
</body>
</html>
```